Brightwell Consulting Business Card Design

Business Card Design for Brightwell Consulting. Brightwell Consulting is a boutique consultancy based in Atlanta, GA., that specializes in marketing strategy, organization planning, and leadership development. We provide solutions for small businesses and startups as well as Summit 400 companies.

http://brightwellconsulting.example/

Target Market(s)

We provide solutions for small businesses and startups as well as Summit 400 companies.

Industry/Entity Type

Consulting

Contact Information for Business Card

Two sided business card with priority on contact information, logo, tag line (Inspiration to Dream More, Do More, Become More)

Colors

Designer to choose colors to be used in the design.

Requirements
Must have
• contact information, logo, tag line (Inspiration to Dream More, Do More, Become More)
• Simple no over communication.
Nice to have
• I would like to see different placements of logo and creative use of both sides of the card
Should not have
• Do not put too much information on the card.

```html
<!DOCTYPE html>
<html lang="en">
<head>
<meta charset="utf-8">
<title>Brightwell Consulting Business Card</title>
<link rel="stylesheet" href="https://fonts.googleapis.com/css2?family=Roboto:wght@400;500&family=Roboto+Condensed:wght@500&display=swap">
<style>
  :root {
    --backdrop: #6e4a31;
    --card: #242424;
    --card-edge: #1a1a1a;
    --card-pattern: #2b2b2b;
    --ink: #f4f4f4;
    --ink-muted: #b9b9b9;
    --divider: #4a4a4a;
  }
  * { margin: 0; padding: 0; box-sizing: border-box; }
  html, body { width: 1200px; height: 960px; overflow: hidden; }
  body {
    position: relative;
    background: var(--backdrop);
    font-family: "Roboto", Arial, sans-serif;
    color: var(--ink);
  }
  .card {
    position: absolute;
    background: var(--card);
    box-shadow: 0 4px 12px rgba(0,0,0,0.45);
  }
  .card-front {
    left: 322px; top: 100px; width: 606px; height: 360px;
    background: linear-gradient(135deg, var(--card-pattern), var(--card-edge));
  }
  .card-back { left: 320px; top: 493px; width: 600px; height: 342px; }

  .wordmark {
    display: flex; align-items: center; gap: 10px;
    font-weight: 500; color: var(--ink); white-space: nowrap;
  }
  .wordmark-mark { width: 14px; height: 14px; background: var(--ink); flex: none; }

  .card-front .wordmark {
    position: absolute; left: 0; right: 0; top: 150px;
    justify-content: center; font-size: 38px;
  }
  .tagline {
    position: absolute; left: 0; right: 0; top: 289px;
    text-align: center; font-size: 14px; color: var(--ink);
  }

  .card-back .wordmark {
    position: absolute; left: 36px; top: 157px; font-size: 24px; gap: 8px;
  }
  .card-back .wordmark-mark { width: 11px; height: 11px; }
  .divider {
    position: absolute; left: 290px; top: 110px; width: 1px; height: 120px;
    background: var(--divider);
  }
  .contact { position: absolute; left: 319px; top: 114px; }
  .contact-name {
    font-family: "Roboto Condensed", Arial, sans-serif; font-weight: 500;
    font-size: 20px; color: var(--ink-muted); letter-spacing: 0.2px;
  }
  .contact-role { font-size: 15.5px; font-weight: 500; margin-top: 2px; }
  .contact-list { list-style: none; margin-top: 11px; font-size: 14px; line-height: 19px; }
  .contact-list li { display: flex; align-items: center; gap: 9px; }
  .contact-list svg { width: 12px; height: 12px; fill: var(--ink-muted); flex: none; }
</style>
</head>
<body>
  <section class="card card-front" role="img" aria-label="Dark card face with subtle tone-on-tone grid pattern">
    <div class="wordmark"><span class="wordmark-mark"></span>Brightwell Consulting</div>
    <p class="tagline">Inspiration to Dream More, Do More, Become More</p>
  </section>

  <section class="card card-back">
    <div class="wordmark"><span class="wordmark-mark"></span>Brightwell Consulting</div>
    <div class="divider"></div>
    <div class="contact">
      <h1 class="contact-name">DARREN HOLLOWAY</h1>
      <p class="contact-role">Founder/Managing Director</p>
      <ul class="contact-list">
        <li>
          <svg viewBox="0 0 24 24" aria-hidden="true"><path d="M6.6 10.8a15.1 15.1 0 0 0 6.6 6.6l2.2-2.2a1 1 0 0 1 1-.25 11.4 11.4 0 0 0 3.6.57 1 1 0 0 1 1 1V20a1 1 0 0 1-1 1A17 17 0 0 1 3 4a1 1 0 0 1 1-1h3.5a1 1 0 0 1 1 1c0 1.25.2 2.45.57 3.57a1 1 0 0 1-.25 1z"/></svg>
          555-014-2290
        </li>
        <li>
          <svg viewBox="0 0 24 24" aria-hidden="true"><path d="M2 5h20v14H2z M4 7v.5l8 5 8-5V7l-8 5z" fill-rule="evenodd"/></svg>
          darren@brightwellconsulting.example
        </li>
        <li>
          <svg viewBox="0 0 24 24" aria-hidden="true"><circle cx="12" cy="12" r="10"/></svg>
          brightwellconsulting.example
        </li>
      </ul>
    </div>
  </section>
</body>
</html>
```